Fin-Tech Firm Captivating Business Card Design

We need a logo design as well to compliment this business card.

We are a new startup based in Singapore called 'Pardeo Technologies'.

We develop an array of financial solutions ranging from payment convenience to forex trading and remittance.

Our initial product is Mavo - an application which allows user to pre-order food items which would be ready for pickup upon arrival.

We would like to see designs being in black and silver or whatever that looks appealing and exudes a fun and professional feel.

We're not picky as long as it doesn't look like common business cards will do.

I do have a current logo which i do not really like. It will be attached for reference sake

Info:

Pardeo Technologies Pte. Ltd.
Company Registration no. 208716392K

FILE TO BE IN .AI and .PSD

Target Market(s)

-F&B (Online-Ordering)
-Finance(P2P Lending and Forex)

Industry/Entity Type

Finance

Contact Information for Business Card

Name
Position
Contact
Email
Address: 27 Corwen Street, Meridale Tower, #14-05 Singapore 058214

Harlan Webb
Founder, Managing Director
+65 90481736
harlan.w@pardeotech.com

Wei Tan
Founder, Executive Director
+65 93570284
wei.t@pardeotech.com

Logo Text

Pardeo Technologies

Font styles to use
Sans Serif

Requirements
Must have
• Something that has word play about link pard
• Minimalistic but also something that catches The Eye
• Gold/silver on white/black might be nice
• Animal logo ; horse, eagle, bull or bear
Nice to have
• Just make it look fun and cute
• Just a suggestion to make the Y of pardeo stand out
Should not have
• Any landmarks of singapore
• Exclude Pte. Ltd.

```html
<!DOCTYPE html>
<html lang="en">
<head>
<meta charset="utf-8">
<title>Pardeo Technologies – Business Card</title>
<link href="https://fonts.googleapis.com/css2?family=Open+Sans:wght@400;600;700&display=swap" rel="stylesheet">
<style>
  :root {
    --backdrop: #e9e9ea;
    --card-black: #131313;
    --silver: #cfcfcf;
    --silver-soft: #a9a9a9;
    --shadow: rgba(0, 0, 0, 0.22);
  }
  * { margin: 0; padding: 0; box-sizing: border-box; }
  html, body {
    width: 1200px;
    height: 801px;
    overflow: hidden;
    background: var(--backdrop);
    font-family: "Open Sans", Arial, sans-serif;
  }
  .stage {
    position: relative;
    width: 1200px;
    height: 801px;
  }
  .card {
    position: absolute;
    top: 258px;
    width: 500px;
    height: 286px;
    background: var(--card-black);
    border-radius: 3px;
    box-shadow: 0 14px 30px var(--shadow);
    color: var(--silver);
  }
  .card--back { left: 70px; }
  .card--front { left: 630px; }

  /* Back side */
  .back-brand {
    position: absolute;
    left: 0; right: 0;
    top: 104px;
    text-align: center;
    font-size: 30px;
    font-weight: 600;
    letter-spacing: 3px;
    color: var(--silver);
  }
  .back-web {
    position: absolute;
    left: 0; right: 0;
    bottom: 28px;
    text-align: center;
    font-size: 14px;
    letter-spacing: 2px;
    color: var(--silver);
  }

  /* Front side */
  .front-brand {
    position: absolute;
    left: 34px;
    top: 104px;
    font-size: 25px;
    font-weight: 400;
    letter-spacing: 3px;
    line-height: 1.25;
    text-transform: uppercase;
    color: var(--silver);
  }
  .contact {
    position: absolute;
    left: 292px;
    top: 70px;
    width: 200px;
    font-size: 10.5px;
    line-height: 1.65;
    color: var(--silver-soft);
  }
  .contact__name {
    font-size: 15px;
    font-weight: 700;
    color: var(--silver);
    line-height: 1.3;
  }
  .contact__role { margin-bottom: 4px; }
  .contact__line {
    display: flex;
    align-items: center;
    gap: 6px;
  }
  .contact__icon {
    width: 10px;
    height: 10px;
    flex: none;
  }
  .contact__address {
    margin-top: 4px;
    text-transform: uppercase;
  }
</style>
</head>
<body>
  <main class="stage">
    <section class="card card--back" aria-label="Business card back">
      <div class="back-brand">Pardeo Technologies</div>
      <div class="back-web">www.pardeotech.com</div>
    </section>

    <section class="card card--front" aria-label="Business card front">
      <div class="front-brand">Pardeo<br>Technologies</div>
      <div class="contact">
        <div class="contact__name">Harlan Webb</div>
        <div class="contact__role">Founder | Managing Director</div>
        <div class="contact__line">
          <svg class="contact__icon" viewBox="0 0 10 10" aria-hidden="true">
            <rect width="10" height="10" rx="1.5" fill="#cfcfcf"/>
            <path d="M3 2.2 4.2 3.6 3.5 4.4Q4.4 6 5.8 6.6L6.6 5.8 7.9 7 7.2 8Q4.5 7.7 2.2 3.2Z" fill="#131313"/>
          </svg>
          <span>+65 90481736</span>
        </div>
        <div class="contact__line">
          <svg class="contact__icon" viewBox="0 0 10 10" aria-hidden="true">
            <rect width="10" height="10" rx="1.5" fill="#cfcfcf"/>
            <rect x="2" y="3" width="6" height="4.2" fill="none" stroke="#131313" stroke-width="0.8"/>
            <path d="M2 3 5 5.4 8 3" fill="none" stroke="#131313" stroke-width="0.8"/>
          </svg>
          <span>harlan.w@pardeotech.com</span>
        </div>
        <div class="contact__address">27 Corwen Street, Meridale Tower<br>#14-05 Singapore 058214</div>
      </div>
    </section>
  </main>
</body>
</html>
```